Business Card and Letterhead Design for Public Accounting Firm

Business card and letterhead design for a CPA Firm located in Orange County, CA. We're looking for a modern and professional design utilizing our existing logo. We'd like a clean "less is more" look, but also something that catches the eye. We provide a high level of service to our clients. Open to single or double sided business cards.

Additional info: color numbers on logo
Blue :
R 0
G 83
B 125

#00537D

Silver :

R 154
G 154
B 154

#9A9A9A

Target Market(s)

Businesses and individuals

Industry/Entity Type

Accounting

Contact Information for Business Card

Moss Whitfield & Danby LLP - 4827 Larkspur Vale Road, Irvine, CA 92614 - (949)731-2864 - mwdaccts.example

Font styles to use
Serif
Sans Serif
Other font styles liked:
• See font file uploaded

Colors
0054AA
0677BA
7BADD7
CADEEF
E8F1F8

Requirements
Nice to have
• Possibly use the font file provided which matches our logo, but adjust to be not in all caps

```html
<!DOCTYPE html>
<html lang="en">
<head>
<meta charset="utf-8">
<title>Moss Whitfield &amp; Danby LLP — Business Card</title>
<link href="https://fonts.googleapis.com/css2?family=Cinzel:wght@400;500&family=Arimo:wght@400;700&display=swap" rel="stylesheet">
<style>
  :root{
    --bg:#ebecec;
    --card:#0a4d7c;
    --card-deep:#063e66;
    --white:#ffffff;
    --silver:#b9c1c8;
    --silver-dim:#8ea3b5;
    --rule:#5f85a4;
    --accent:#2f7fb8;
  }
  *{margin:0;padding:0;box-sizing:border-box}
  html,body{width:1200px;height:802px;overflow:hidden;background:var(--bg)}
  .stage{position:relative;width:1200px;height:802px}
  .card{
    position:absolute;top:251px;width:525px;height:300px;
    background:var(--card);overflow:hidden;
    box-shadow:0 6px 18px rgba(0,0,0,.18);
  }
  .card--front{left:50px}
  .card--back{left:625px;background:linear-gradient(160deg,var(--card) 0%,var(--card-deep) 100%)}

  /* front */
  .brand{position:absolute;left:60px;top:58px;display:flex;align-items:center;gap:16px}
  .brand__dot{width:34px;height:34px;border-radius:50%;background:var(--white)}
  .brand__rule{width:1px;height:58px;background:var(--rule)}
  .brand__name{font-family:"Cinzel",serif;color:var(--silver);font-size:17px;letter-spacing:2px;line-height:1.25}
  .person{position:absolute;left:60px;top:150px;text-align:right;width:150px}
  .person__name{font-family:"Arimo",sans-serif;font-weight:700;color:var(--white);font-size:16px;letter-spacing:.5px;text-transform:uppercase}
  .person__role{font-family:"Arimo",sans-serif;color:var(--silver-dim);font-size:13px;margin-top:3px}
  .split{position:absolute;left:226px;top:140px;width:1px;height:70px;background:var(--rule)}
  .contact{position:absolute;left:242px;top:140px;list-style:none;font-family:"Arimo",sans-serif;font-size:13px;color:var(--silver)}
  .contact li{display:flex;align-items:center;gap:8px;height:23px}
  .contact svg{width:12px;height:12px;fill:var(--white)}
  .address{position:absolute;left:60px;bottom:34px;font-family:"Arimo",sans-serif;font-size:13px;color:var(--silver-dim)}

  /* back */
  .back-name{position:absolute;left:40px;top:46px;font-family:"Cinzel",serif;color:var(--silver);font-size:36px;letter-spacing:4px;line-height:1.2}
  .back-disc{position:absolute;right:-70px;bottom:-120px;width:300px;height:300px;border-radius:50%;background:var(--accent);opacity:.35}
</style>
</head>
<body>
<main class="stage">
  <section class="card card--front" aria-label="Business card front">
    <div class="brand">
      <span class="brand__dot"></span>
      <span class="brand__rule"></span>
      <p class="brand__name">Moss Whitfield<br>&amp; Danby LLP</p>
    </div>
    <div class="person">
      <p class="person__name">Daniel Hart</p>
      <p class="person__role">Manager</p>
    </div>
    <span class="split"></span>
    <ul class="contact">
      <li><svg viewBox="0 0 12 12"><path d="M3 1l2 2.5-1.2 1.2a6 6 0 0 0 3.5 3.5L8.5 7 11 9l-1.5 2C5 11 1 7 1 2.5z"/></svg>(949)731-2864</li>
      <li><svg viewBox="0 0 12 12"><path d="M1 2.5h10v7H1zM1.5 3l4.5 3.5L10.5 3" stroke="#0a4d7c" stroke-width=".8"/></svg>office@mwdaccts.example</li>
      <li><svg viewBox="0 0 12 12"><circle cx="6" cy="6" r="5"/><path d="M1 6h10M6 1c-2.5 3-2.5 7 0 10M6 1c2.5 3 2.5 7 0 10" stroke="#0a4d7c" stroke-width=".8" fill="none"/></svg>mwdaccts.example</li>
    </ul>
    <p class="address">4827 Larkspur Vale Road, Irvine, CA 92614</p>
  </section>

  <section class="card card--back" aria-label="Business card back">
    <span class="back-disc"></span>
    <p class="back-name">Moss Whitfield<br>&amp; Danby LLP</p>
  </section>
</main>
</body>
</html>
```